Refrigeration & Air Conditioning modern and appealing

We want to design a business card that is modern and appealing using existing logo supplied

Front card
Residential Commercial Diary
RTA : AU071523
Licence L258907

Back card
Marcus Ovenly
Director
0491 352 406
info@frostvalecooling.com.au
www.frostvalecooling.com.au
• Air Conditioning
• Cool Rooms & Refrigeration
• Installation
• Service & Repair
• Preventative Maintenance

We offer 24/7 emergency service

```html
<!DOCTYPE html>
<html lang="en">
<head>
<meta charset="utf-8">
<title>Frostvale Business Card</title>
<link href="https://fonts.googleapis.com/css2?family=Montserrat:wght@400;500;600;700;800&display=swap" rel="stylesheet">
<style>
  :root {
    --stage: #2b2b2d;
    --card: #0d0d0f;
    --white: #ffffff;
    --violet: #a24ee8;
    --violet-soft: #b98cf5;
    --lavender: #c6c6ff;
    --rule: #9a9aa6;
  }
  * { box-sizing: border-box; margin: 0; padding: 0; }
  html, body { width: 1200px; height: 939px; overflow: hidden; }
  body {
    background: var(--stage);
    font-family: "Montserrat", sans-serif;
    color: var(--white);
    position: relative;
  }
  .card {
    position: absolute;
    width: 620px;
    height: 354px;
    background: var(--card);
    box-shadow: 0 14px 34px rgba(0,0,0,.55);
    overflow: hidden;
  }
  /* Front */
  .card-front { left: 80px; top: 70px; }
  .brand-front {
    position: absolute; left: 0; right: 0; top: 128px;
    display: flex; align-items: center; justify-content: center; gap: 18px;
  }
  .brand-dot {
    width: 54px; height: 54px; border-radius: 50%;
    background: var(--violet);
  }
  .brand-name {
    font-weight: 800; font-size: 54px; letter-spacing: 1px;
    color: var(--white); text-transform: uppercase;
  }
  .credentials {
    position: absolute; left: 0; right: 0; bottom: 34px;
    text-align: center; font-size: 13px; font-weight: 500; letter-spacing: .3px;
  }
  .credentials .sep { color: var(--violet-soft); margin: 0 4px; }

  /* Back */
  .card-back { left: 500px; top: 500px; }
  .brand-back {
    position: absolute; left: 52px; top: 54px; width: 170px;
    display: flex; flex-direction: column; align-items: center; gap: 12px;
  }
  .brand-back .brand-dot { width: 104px; height: 104px; }
  .brand-back .brand-name { font-size: 20px; letter-spacing: 1px; }
  .divider {
    position: absolute; left: 240px; top: 40px; width: 1px; height: 150px;
    background: var(--rule);
  }
  .contact { position: absolute; left: 262px; top: 40px; }
  .person-name {
    font-weight: 700; font-size: 26px; color: var(--violet-soft);
    text-transform: uppercase; letter-spacing: .5px;
  }
  .person-role { font-size: 14px; font-weight: 500; margin: 2px 0 14px; }
  .contact-list { list-style: none; display: flex; flex-direction: column; gap: 6px; }
  .contact-list li {
    display: flex; align-items: center; gap: 8px; font-size: 14px; font-weight: 500;
  }
  .contact-list svg { width: 14px; height: 14px; flex: none; }
  .services { position: absolute; left: 0; right: 0; top: 222px; text-align: center; }
  .emergency {
    font-weight: 700; font-size: 14px; color: var(--violet-soft);
    text-transform: uppercase; letter-spacing: .5px; margin-bottom: 6px;
  }
  .service-line { font-size: 14px; font-weight: 500; line-height: 1.45; }
  .accent-band {
    position: absolute; left: 0; right: 0; bottom: 0; height: 20px;
    background: linear-gradient(90deg, var(--violet), var(--lavender));
  }
</style>
</head>
<body>
  <section class="card card-front" aria-label="Business card front">
    <div class="brand-front">
      <span class="brand-dot"></span>
      <span class="brand-name">Frostvale</span>
    </div>
    <p class="credentials">RTA : AU071523<span class="sep">•</span>Residential Commercial Diary<span class="sep">•</span>Licence L258907</p>
  </section>

  <section class="card card-back" aria-label="Business card back">
    <div class="brand-back">
      <span class="brand-dot"></span>
      <span class="brand-name">Frostvale</span>
    </div>
    <div class="divider"></div>
    <div class="contact">
      <h1 class="person-name">Marcus Ovenly</h1>
      <p class="person-role">Director</p>
      <ul class="contact-list">
        <li>
          <svg viewBox="0 0 24 24" fill="#b98cf5" aria-hidden="true"><path d="M6.6 10.8a15.1 15.1 0 0 0 6.6 6.6l2.2-2.2a1 1 0 0 1 1-.25 11.4 11.4 0 0 0 3.6.57 1 1 0 0 1 1 1V20a1 1 0 0 1-1 1A17 17 0 0 1 3 4a1 1 0 0 1 1-1h3.5a1 1 0 0 1 1 1c0 1.25.2 2.45.57 3.57a1 1 0 0 1-.25 1z"/></svg>
          0491 352 406
        </li>
        <li>
          <svg viewBox="0 0 24 24" fill="#b98cf5" aria-hidden="true"><path d="M2 5h20v14H2z" fill="none" stroke="#b98cf5" stroke-width="2"/><path d="M2 5l10 8 10-8" fill="none" stroke="#b98cf5" stroke-width="2"/></svg>
          info@frostvalecooling.com.au
        </li>
        <li>
          <svg viewBox="0 0 24 24" fill="none" stroke="#b98cf5" stroke-width="2" aria-hidden="true"><circle cx="12" cy="12" r="9"/><path d="M3 12h18M12 3c3 3 3 15 0 18M12 3c-3 3-3 15 0 18"/></svg>
          www.frostvalecooling.com.au
        </li>
      </ul>
    </div>
    <div class="services">
      <p class="emergency">We offer 24/7 emergency service</p>
      <p class="service-line">• Air Conditioning • Cool Rooms &amp; Refrigeration • Installation</p>
      <p class="service-line">• Service &amp; Repair • Preventative Maintenance</p>
    </div>
    <div class="accent-band"></div>
  </section>
</body>
</html>
```